Echoes Beyond The Willow Poster

So Last year One of the Great Designers from here Came up with a poster for my Events... But Now it is Time to freshen it up.. I have attached the original poster.. I would like the Same wording.. Same Picture of me,. Just fresh Design and colours for the new event year ahead.
This Poster Will be used in Theatres and Hall to Advertise our Event so it needs to stand out but still remain classy
I would Also need The Final Version to be delivered in PhotoShop Version so That I Can Alter Things like the Venue Name, Date, and Ticket Details,, As they change all the time.
Industry/Entity Type
Events
Colors
Designer to choose colors to be used in the design.
Look and feel
Each slider illustrates characteristics of the customer's brand and the style your logo design should communicate.

```html
<!DOCTYPE html>
<html lang="en">
<head>
<meta charset="UTF-8">
<title>Echoes Beyond The Willow – An Evening of Mediumship</title>
<link rel="stylesheet" href="https://fonts.googleapis.com/css2?family=Cormorant+Garamond:ital,wght@0,300;0,400;1,300;1,400&family=Josefin+Sans:wght@200;300;400&display=swap">
<style>
  :root {
    --midnight: #120d20;
    --plum: #2a1738;
    --violet: #4a2a5c;
    --rose: #c98a7d;
    --gold: #d6b46c;
    --gold-soft: rgba(214,180,108,0.55);
    --ivory: #f4ede1;
    --mist: #b9a9c4;
  }
  * { margin: 0; padding: 0; box-sizing: border-box; }
  html, body { width: 927px; height: 1200px; overflow: hidden; background: var(--midnight); }
  .poster {
    position: relative;
    width: 927px; height: 1200px;
    background:
      radial-gradient(ellipse 70% 45% at 50% 42%, rgba(106,60,122,0.55), transparent 75%),
      linear-gradient(to bottom, var(--plum) 0%, var(--midnight) 70%, #0a0714 100%);
    color: var(--ivory);
    font-family: "Josefin Sans", sans-serif;
    font-weight: 300;
    text-align: center;
  }
  .frame {
    position: absolute; inset: 26px;
    border: 1px solid var(--gold-soft);
  }
  .frame::after {
    content: ""; position: absolute; inset: 8px;
    border: 1px solid rgba(214,180,108,0.25);
  }
  .eyebrow {
    position: absolute; top: 74px; left: 0; width: 100%;
    font-size: 17px; letter-spacing: 7px; text-transform: uppercase;
    color: var(--gold);
  }
  .title {
    position: absolute; top: 108px; left: 0; width: 100%;
    font-family: "Cormorant Garamond", serif; font-weight: 300;
    line-height: 1;
  }
  .title .line-one { display: block; font-size: 68px; letter-spacing: 8px; text-transform: uppercase; }
  .title .line-two { display: block; margin-top: 6px; font-size: 62px; letter-spacing: 4px; }
  .title .joiner { font-style: italic; font-size: 44px; letter-spacing: 1px; color: var(--gold); text-transform: none; }
  .arch-line {
    position: absolute; left: 197px; top: 283px; width: 533px; height: 527px;
    border: 1px solid var(--gold-soft); border-bottom: none;
    border-radius: 267px 267px 0 0;
  }
  .portrait {
    position: absolute; left: 212px; top: 298px; width: 503px; height: 512px;
    border-radius: 252px 252px 0 0;
    background:
      radial-gradient(ellipse 30% 24% at 46% 28%, rgba(216,150,128,0.85), transparent 72%),
      radial-gradient(ellipse 55% 50% at 50% 85%, rgba(14,10,26,0.95), transparent 75%),
      linear-gradient(to bottom, #6b4a7e 0%, #3b2450 55%, var(--midnight) 100%);
  }
  .billing {
    position: absolute; top: 826px; left: 0; width: 100%;
    font-family: "Cormorant Garamond", serif; font-style: italic; font-weight: 400;
    font-size: 30px; letter-spacing: 1px; color: var(--mist);
  }
  .performer {
    position: absolute; top: 872px; left: 0; width: 100%;
    font-size: 70px; font-weight: 300; letter-spacing: 10px; line-height: 1;
  }
  .divider {
    position: absolute; top: 964px; left: 313px; width: 300px; height: 12px;
  }
  .date {
    position: absolute; top: 992px; left: 0; width: 100%;
    font-size: 34px; font-weight: 300; letter-spacing: 8px; color: var(--gold);
  }
  .date .day { color: var(--ivory); }
  .details {
    position: absolute; top: 1080px; left: 70px; width: 787px; height: 60px;
    border-top: 1px solid rgba(214,180,108,0.3);
    display: flex; align-items: center; justify-content: space-between;
    padding-top: 14px;
    font-size: 22px; letter-spacing: 2px;
  }
  .tickets { display: flex; align-items: center; gap: 10px; }
  .tickets .label { color: var(--gold); text-transform: uppercase; font-size: 17px; letter-spacing: 4px; }
  .tickets .number { font-size: 24px; letter-spacing: 3px; }
  .tickets svg { width: 18px; height: 18px; }
</style>
</head>
<body>
<main class="poster">
  <div class="frame"></div>

  <p class="eyebrow">an evening of mediumship</p>
  <h1 class="title">
    <span class="line-one">Echoes Beyond</span>
    <span class="line-two"><span class="joiner">the</span> WILLOW</span>
  </h1>

  <div class="arch-line"></div>
  <div class="portrait" role="img" aria-label="Portrait photograph of the medium in a dark jacket, reaching one hand toward the viewer"></div>

  <p class="billing">renowned spiritualist medium</p>
  <h2 class="performer">RHYS MORWEN</h2>

  <svg class="divider" viewBox="0 0 300 12" aria-hidden="true">
    <line x1="0" y1="6" x2="130" y2="6" stroke="#d6b46c" stroke-width="1" opacity="0.6"/>
    <circle cx="150" cy="6" r="4" fill="none" stroke="#d6b46c" stroke-width="1"/>
    <line x1="170" y1="6" x2="300" y2="6" stroke="#d6b46c" stroke-width="1" opacity="0.6"/>
  </svg>

  <p class="date">MON <span class="day">21st</span> NOV</p>

  <footer class="details">
    <span class="venue">Harbour theatre Pontfaen</span>
    <span class="tickets">
      <svg viewBox="0 0 24 24" aria-hidden="true"><path d="M6.6 10.8a15 15 0 0 0 6.6 6.6l2.2-2.2a1 1 0 0 1 1-.25 11.4 11.4 0 0 0 3.6.57 1 1 0 0 1 1 1V20a1 1 0 0 1-1 1A17 17 0 0 1 3 4a1 1 0 0 1 1-1h3.5a1 1 0 0 1 1 1c0 1.25.2 2.45.57 3.57a1 1 0 0 1-.25 1z" fill="#d6b46c"/></svg>
      <span class="label">tickets</span>
      <span class="number">01632 960418</span>
    </span>
  </footer>
</main>
</body>
</html>
```